label bath salt on glass bottle

for our bath salts (Flavours Rose, Lavender, Lemongras, mountain herbs, Mint, Cashmere) we need a label in the size of 50mm height an 55mm wide.

Target Market(s)

Prestige stores

Font styles to use
Serif
Script

Colors

Designer to choose colors to be used in the design.

Requirements
Must have
• Name of the label:
• Headline: Badesalz (can be also written in two words) Bade Salz
• Describtion of the sel: Totes Meer (comes from Dead Sea)
• Name of the different fragrances:
• Rose
• Pfingstrose (Peony)
• Lemongras
• Alpenkräuter (mountain herbs)
• Minze (mint)
• Cashmere
• Lavendel (lavender)
Nice to have
• Made with love in Switzerland
• Logos:
• Use our LOGO in the attachment or just
• PENIVO
• Switzerland

```html
<!DOCTYPE html>
<html lang="de">
<head>
<meta charset="utf-8">
<title>PENIVO Rose Badesalz – Etikett</title>
<link rel="stylesheet" href="https://fonts.googleapis.com/css2?family=Alegreya:ital,wght@0,400;0,500;1,400&family=Courgette&display=swap">
<style>
  :root {
    --canvas: #f2f2f2;
    --rose-red: #e3302f;
    --rose-red-deep: #d62a2b;
    --blush: #f2a0a0;
    --blush-soft: #f7c9c9;
    --paper: #fbf8f6;
    --white: #ffffff;
  }
  * { margin: 0; padding: 0; box-sizing: border-box; }
  html, body {
    width: 1200px;
    height: 872px;
    overflow: hidden;
    background: var(--canvas);
  }
  .label {
    position: absolute;
    left: 390px;
    top: 136px;
    width: 420px;
    height: 600px;
    background: var(--paper);
    border: 12px solid var(--blush);
    font-family: "Alegreya", serif;
    color: var(--rose-red);
  }
  .label__pattern {
    position: absolute;
    left: 0; top: 0;
    width: 100%;
    height: 294px;
    background: linear-gradient(160deg, var(--rose-red) 0%, var(--rose-red-deep) 100%);
  }
  .brand-name {
    position: absolute;
    left: 0; right: 0;
    top: 112px;
    text-align: center;
    font-family: "Alegreya", serif;
    font-weight: 500;
    font-size: 58px;
    letter-spacing: 3px;
    color: var(--white);
    line-height: 1;
  }
  .fragrance-mark {
    position: absolute;
    left: 162px;
    top: 253px;
    width: 72px;
    height: 72px;
    border-radius: 50%;
    background: var(--rose-red);
    border: 3px solid var(--white);
  }
  .fragrance-name {
    position: absolute;
    left: 0; right: 0;
    top: 352px;
    text-align: center;
    font-size: 50px;
    font-weight: 400;
    letter-spacing: 2px;
    line-height: 1;
  }
  .fragrance-rule {
    position: absolute;
    left: 100px;
    width: 196px;
    top: 408px;
    height: 1px;
    background: var(--rose-red);
  }
  .product-type {
    position: absolute;
    left: 0; right: 0;
    top: 414px;
    text-align: center;
    font-size: 19px;
    letter-spacing: 10px;
    padding-left: 10px;
    line-height: 1.2;
  }
  .origin-note {
    position: absolute;
    left: 54px;
    top: 455px;
    width: 288px;
    height: 70px;
    border: 2px solid var(--blush);
    border-radius: 4px;
    display: flex;
    align-items: center;
    justify-content: center;
    text-align: center;
    font-family: "Courgette", cursive;
    font-size: 22px;
    line-height: 1.05;
    color: var(--blush);
  }
  .origin-note::before {
    content: "";
    position: absolute;
    inset: 4px;
    border: 1px solid var(--blush-soft);
    border-radius: 2px;
  }
  .salt-source {
    position: absolute;
    left: 0; right: 0;
    top: 548px;
    text-align: center;
    font-style: italic;
    font-size: 12px;
    color: var(--rose-red);
  }
</style>
</head>
<body>
  <main class="label">
    <div class="label__pattern" role="img" aria-label="Leaf pattern in shades of red"></div>
    <h1 class="brand-name">PENIVO</h1>
    <div class="fragrance-mark" role="img" aria-label="Rose blossom emblem"></div>
    <h2 class="fragrance-name">ROSE</h2>
    <div class="fragrance-rule"></div>
    <p class="product-type">BADESALZ</p>
    <p class="origin-note">Made with love in<br>Switzerland</p>
    <p class="salt-source">Description of the sel: Totes Meer</p>
  </main>
</body>
</html>
```